IT Consulting Business Card Design

We need a business card on our company name....which is a IT consulting and staffing company. We also train masters graduates in various IT courses. 70% of the time these cards will be handed out to the graduate students at the universities. 30% for our clients and business partners. We are uploading our company logo...would like to see something that matches our logo or blends with it. Please visit www.brightvaleworks.com for more details on logo and colors.

Target Market(s)

70% of the time these cards will be handed out to the graduate students at the universities. 30% for our clients and business partners.

Industry/Entity Type

Business

Contact Information for Business Card

Ravi Kondamuri
Vice-President
Bright Vale Works Inc
3807 Morrow Lane, Suite 412
East Brookridge, NJ 07315
ravi@brightvaleworks.com
Office : 1-866-219-3840 X 515
Cell number : 732-581-9034

Requirements
Nice to have
• may be company logo and name on the back of the card and detials on the other side...just a thought..!!

```html
<!DOCTYPE html>
<html lang="en">
<head>
<meta charset="utf-8">
<title>Bright Vale Works – Business Card</title>
<link href="https://fonts.googleapis.com/css2?family=PT+Sans:wght@400;700&display=swap" rel="stylesheet">
<style>
  :root {
    --stage: #e9e6e1;
    --card-dark: #1f1f1f;
    --card-dark-edge: #111111;
    --card-light: #ffffff;
    --brand-red: #e0202a;
    --text-white: #ffffff;
    --text-grey: #555555;
    --text-dark: #333333;
    --mark-grey: #d6d6d6;
  }
  * { margin: 0; padding: 0; box-sizing: border-box; }
  html, body {
    width: 1200px; height: 1000px; overflow: hidden;
    background: var(--stage);
    font-family: "PT Sans", Arial, sans-serif;
  }
  .canvas { position: relative; width: 1200px; height: 1000px; }

  .card { position: absolute; box-shadow: 0 10px 24px rgba(0,0,0,0.25); }

  /* Back of card – brand side */
  .card-back {
    left: 170px; top: 95px; width: 625px; height: 325px;
    background: linear-gradient(160deg, #2a2a2a, var(--card-dark) 55%, var(--card-dark-edge));
  }
  .brand-lockup {
    position: absolute; left: 130px; top: 128px;
    display: flex; align-items: center; gap: 22px;
  }
  .brand-dot {
    width: 64px; height: 64px; border-radius: 50%;
    background: var(--brand-red);
  }
  .brand-name {
    font-weight: 700; font-size: 38px; letter-spacing: 0.5px;
    color: var(--text-white); text-transform: uppercase;
  }
  .brand-web {
    position: absolute; left: 0; right: 0; bottom: 26px;
    text-align: center; font-size: 17px; color: var(--text-white);
  }

  /* Front of card – contact side */
  .card-front {
    left: 292px; top: 448px; width: 758px; height: 410px;
    background: var(--card-light); overflow: hidden;
  }
  .person-name {
    position: absolute; left: 36px; top: 42px;
    font-weight: 700; font-size: 25px; color: var(--brand-red);
  }
  .person-role {
    position: absolute; left: 36px; top: 73px;
    font-size: 14px; color: var(--text-grey);
  }
  .address {
    position: absolute; left: 44px; top: 276px;
    font-size: 15px; line-height: 22px; color: var(--text-dark);
  }
  .contact-list {
    position: absolute; left: 46px; top: 324px;
    list-style: none; font-size: 15px; color: var(--text-dark);
  }
  .contact-list li { display: flex; align-items: center; gap: 12px; height: 21px; }
  .contact-icon { width: 16px; height: 16px; flex: none; }
  .corner-disc {
    position: absolute; right: -40px; bottom: -40px;
    width: 300px; height: 300px; border-radius: 50%;
    background: var(--mark-grey);
  }
</style>
</head>
<body>
<main class="canvas">

  <section class="card card-back" aria-label="Card back">
    <div class="brand-lockup">
      <span class="brand-dot"></span>
      <span class="brand-name">Bright Vale Works</span>
    </div>
    <p class="brand-web">www.brightvaleworks.com</p>
  </section>

  <section class="card card-front" aria-label="Card front">
    <h1 class="person-name">Ravi Kondamuri</h1>
    <p class="person-role">Vice-President Bright Vale Works Inc</p>

    <address class="address">
      3807 Morrow Lane,<br>
      Suite 412 East Brookridge, NJ 07315
    </address>

    <ul class="contact-list">
      <li>
        <svg class="contact-icon" viewBox="0 0 16 16" aria-hidden="true">
          <circle cx="8" cy="8" r="8" fill="var(--brand-red)"/>
          <rect x="5.5" y="3.5" width="5" height="9" rx="1" fill="none" stroke="#fff" stroke-width="1.2"/>
          <circle cx="8" cy="10.8" r="0.7" fill="#fff"/>
        </svg>
        <span>732-581-9034</span>
      </li>
      <li>
        <svg class="contact-icon" viewBox="0 0 16 16" aria-hidden="true">
          <circle cx="8" cy="8" r="8" fill="var(--brand-red)"/>
          <path d="M4 6.5 Q8 3.5 12 6.5 L11 8 L9.5 7 L9.5 6 Q8 5.5 6.5 6 L6.5 7 L5 8 Z" fill="#fff"/>
          <rect x="5" y="8.5" width="6" height="3.5" rx="0.6" fill="#fff"/>
        </svg>
        <span>1-866-219-3840 X 515</span>
      </li>
      <li>
        <svg class="contact-icon" viewBox="0 0 16 16" aria-hidden="true">
          <circle cx="8" cy="8" r="8" fill="var(--brand-red)"/>
          <rect x="3.8" y="5" width="8.4" height="6" fill="#fff"/>
          <path d="M3.8 5 L8 8.4 L12.2 5" fill="none" stroke="var(--brand-red)" stroke-width="1"/>
        </svg>
        <span>ravi@brightvaleworks.com</span>
      </li>
    </ul>

    <div class="corner-disc" role="img" aria-label="Large brand mark decoration area"></div>
  </section>

</main>
</body>
</html>
```